Business card design needed

I run a life coaching business.
I coach individuals, businesses & groups.
Our aim is create massive change for our clients.
I would like to see a card that is inspirational, something that provokes the thought of achieving your personal best.
Be your own inspiration is a phrase I am considering using.

Target Market(s)

People who are looking to create a massive change in their lives.

Industry/Entity Type

Life Coaching

Contact Information for Business Card

Harbor Light Coaching
Neil Pardoe
Head Coach
email neil@vorunel.com.au
Mob 0412 586 337

Logo styles of interest
Abstract Logo
Requirements
Must have
• I wouldlike to have a free introductory offer on the reverse side of the card.
It would read something like:
Is coaching for me/you?
Try a free 45 minute session.
Book now call or email for your appointment.

```html
<!DOCTYPE html>
<html lang="en">
<head>
<meta charset="UTF-8">
<title>Harbor Light Coaching – Free Session Offer</title>
<link rel="stylesheet" href="https://fonts.googleapis.com/css2?family=Courier+Prime&display=swap">
<style>
  :root {
    --sage: #9fb9aa;
    --band-green: #156c00;
    --band-shadow: rgba(10, 25, 15, 0.85);
    --text-sage: #a9c6b2;
  }
  html, body {
    margin: 0;
    padding: 0;
    overflow: hidden;
  }
  .card {
    position: relative;
    width: 1200px;
    height: 693px;
    background: var(--sage);
    overflow: hidden;
    font-family: "Courier Prime", "Courier New", monospace;
    color: var(--text-sage);
  }
  .wave-band {
    position: absolute;
    inset: 0;
    width: 1200px;
    height: 693px;
    filter: drop-shadow(10px 12px 8px var(--band-shadow));
  }
  .wave-band path {
    fill: var(--band-green);
  }
  .offer-line {
    position: absolute;
    left: 0;
    width: 1172px;
    margin: 0;
    text-align: center;
    line-height: 1;
    font-weight: 400;
    white-space: nowrap;
  }
  .offer-question {
    top: 292px;
    font-size: 54px;
  }
  .offer-headline {
    top: 340px;
    font-size: 38px;
  }
  .offer-underline {
    position: absolute;
    left: 260px;
    top: 377px;
    width: 650px;
    height: 4px;
    background: var(--text-sage);
  }
  .offer-action {
    top: 388px;
    font-size: 29px;
  }
</style>
</head>
<body>
  <main class="card">
    <svg class="wave-band" viewBox="0 0 1200 693" aria-hidden="true">
      <path d="M54 224 C 200 268, 400 284, 560 280 C 760 273, 950 226, 1154 201 L 1151 448 C 1050 446, 950 440, 892 438 C 760 436, 650 495, 531 491 C 400 488, 300 440, 200 420 C 130 405, 70 400, 47 390 C 45 330, 50 270, 54 224 Z"/>
    </svg>
    <h1 class="offer-line offer-question">IS COACHING FOR YOU?</h1>
    <p class="offer-line offer-headline">TRY A FREE 45 MINUTE SESSION</p>
    <div class="offer-underline"></div>
    <p class="offer-line offer-action">BOOK NOW, CALL OR EMAIL</p>
  </main>
</body>
</html>
```